Design letter head and business card

Hello,

you should design a business card and letter paper for Wolkenfalke Marketing. In German we write this word with K insteat of C.

Company does not have a logo. But in general, we write Wolkenfalke Marketing in 2 lines.
First line red: WOLKENFALKE
Second line gray: MARKETING

Red (or wine red) and Gray / Black are our favorite colors.

Company slogan: "Higher Ground Web Marketing".

Company offers SEO, SEM, SEA, AdWords, Conversion Optimization, Online Markting Consulting ...

The website is old, please do not use this as base for your task.

German letter paper sizes:
Viawable Dimensions : 210 x 297 mm
Needed file dimensions: 212 x 299 mm

Informations to include:

Address:
Wolkenfalke Marketing GmbH
Lindenweg 23
73614 Lindhausen
Germany

Geschäftsführer | CEO: Dietrich Ronnau

Phone: +49 (0) 7364 482 67 05

Fax: +49 (0) 7364 482 67 88

Mail: info@wolkenfalke-marketing.de

Web: www.wolkenfalke-marketing.de

Amtsgericht Halmstett, HRB 736402

Bank: Sonnfelder Bank
IBAN: DE139817325500XXXXXXXX
BIC: GENODES1QTR

Thanks

Dietrich

Target Market(s)

People who likes to win the online marketing game.

Industry/Entity Type

Business

Contact Information for Business Card

Here is the personal text on the card:

Name:
Dietrich Ronnau

Title:
Geschäftsführer | CEO

Address:
Wolkenfalke Marketing GmbH
Lindenweg 23
73614 Lindhausen
Germany

Phone:
+49 (0) 7364 482 67 05

Fax:
+49 (0) 7364 482 67 88

Mail:
ronnau@wolkenfalke-marketing.de

Web:
www.wolkenfalke-marketing.de

Business Card:
Viewable Dimensions: 85 x 55 mm
Needed file dimensions: 87 x 57mm

Font styles to use
Sans Serif

Requirements
Nice to have
• It would be great to see the dynamics of a helicopter.

```html
<!DOCTYPE html>
<html lang="de">
<head>
<meta charset="utf-8">
<title>Wolkenfalke Marketing – Briefpapier</title>
<link rel="stylesheet" href="https://fonts.googleapis.com/css2?family=Roboto+Condensed:wght@400&family=Roboto+Slab:wght@300;400&display=block">
<style>
  :root {
    --brand-red: #e5161b;
    --ink: #1e1e1e;
    --rule: #8a8a8a;
    --paper: #ffffff;
    --backdrop: #e9e7e4;
  }
  html, body {
    margin: 0;
    width: 963px;
    height: 1200px;
    overflow: hidden;
    background: var(--backdrop);
  }
  .letterhead {
    position: absolute;
    left: 50px;
    top: 25px;
    width: 874px;
    height: 1132px;
    background: var(--paper);
    box-shadow: 0 1px 4px rgba(0,0,0,0.15);
    color: var(--ink);
  }
  .brand-dot {
    position: absolute;
    left: 40px;
    top: 30px;
    width: 70px;
    height: 70px;
    border-radius: 50%;
    background: var(--brand-red);
  }
  .brand-name {
    position: absolute;
    left: 148px;
    top: 22px;
    margin: 0;
    font: 400 31px/37px "Roboto Condensed", sans-serif;
    color: var(--brand-red);
    letter-spacing: 0.3px;
  }
  .slogan {
    position: absolute;
    left: 30px;
    top: 103px;
    margin: 0;
    font: 400 24px/30px "Roboto Condensed", sans-serif;
  }
  .divider {
    position: absolute;
    width: 1px;
    background: var(--rule);
  }
  .contact-list {
    position: absolute;
    left: 560px;
    top: 16px;
    margin: 0;
    padding: 0;
    list-style: none;
    font: 300 17.5px/29px "Roboto Slab", sans-serif;
  }
  .contact-list li {
    display: flex;
    align-items: center;
    gap: 10px;
  }
  .icon {
    width: 19px;
    height: 19px;
    fill: var(--brand-red);
    flex: none;
  }
  .icon--outline {
    fill: none;
    stroke: var(--brand-red);
    stroke-width: 1.4;
  }
  .footer {
    font: 300 16.5px/23.5px "Roboto Slab", sans-serif;
  }
  .footer-address {
    position: absolute;
    left: 47px;
    top: 1026px;
    margin: 0;
    font-style: normal;
  }
  .footer-address .icon {
    position: absolute;
    left: -27px;
    top: 1px;
  }
  .footer-register {
    position: absolute;
    left: 335px;
    top: 1044px;
    margin: 0;
  }
  .footer-bank {
    position: absolute;
    right: 22px;
    top: 1020px;
    margin: 0;
    text-align: right;
    line-height: 28px;
  }
  .footer-bank .label { color: var(--brand-red); }
</style>
</head>
<body>
<main class="letterhead">
  <header>
    <span class="brand-dot" aria-hidden="true"></span>
    <h1 class="brand-name">WOLKENFALKE<br>MARKETING</h1>
    <p class="slogan">Higher Ground Web Marketing</p>
    <span class="divider" style="left:548px;top:20px;height:115px"></span>
    <ul class="contact-list">
      <li>
        <svg class="icon" viewBox="0 0 20 20" aria-hidden="true"><circle cx="10" cy="10" r="9" fill="none" stroke="#e5161b" stroke-width="1.6"/><path d="M7 5.5c.6-.4 1.2-.2 1.5.4l.6 1.3c.2.5 0 1-.4 1.3l-.5.3c.5 1.2 1.4 2.1 2.5 2.6l.4-.5c.3-.4.9-.5 1.3-.3l1.2.7c.5.3.6 1 .2 1.5-.8 1-2 1.1-3.2.5C8.4 12.2 6.9 10.5 6.3 8.3c-.3-1.2 0-2.2.7-2.8z"/></svg>
        +49 (0) 7364 482 67 05
      </li>
      <li>
        <svg class="icon" viewBox="0 0 20 20" aria-hidden="true"><rect x="5" y="1" width="10" height="6"/><rect x="1" y="7" width="18" height="8" rx="1.5"/><rect x="5" y="12" width="10" height="7" fill="#fff" stroke="#e5161b" stroke-width="1.5"/></svg>
        +49 (0) 7364 482 67 88
      </li>
      <li>
        <svg class="icon" viewBox="0 0 20 20" aria-hidden="true"><rect x="1" y="4" width="18" height="12" rx="1"/><path d="M1.5 5l8.5 6 8.5-6" fill="none" stroke="#fff" stroke-width="1.5"/></svg>
        info@wolkenfalke-marketing.de
      </li>
      <li>
        <svg class="icon icon--outline" viewBox="0 0 20 20" aria-hidden="true"><circle cx="10" cy="10" r="8.5"/><ellipse cx="10" cy="10" rx="3.8" ry="8.5"/><path d="M1.5 10h17M3 5.5h14M3 14.5h14"/></svg>
        www.wolkenfalke-marketing.de
      </li>
    </ul>
  </header>

  <footer class="footer">
    <address class="footer-address">
      <svg class="icon" viewBox="0 0 20 20" aria-hidden="true"><path d="M10 1.5L0.5 10h2.8v8h5v-5h3.4v5h5v-8h2.8z"/></svg>
      Wolkenfalke Marketing GmbH<br>
      Lindenweg 23<br>
      73614 Lindhausen<br>
      Germany
    </address>
    <span class="divider" style="left:306px;top:1027px;height:81px"></span>
    <p class="footer-register">Amtsgericht Halmstett,<br>HRB 736402</p>
    <span class="divider" style="left:540px;top:1027px;height:81px"></span>
    <p class="footer-bank">
      <span class="label">Bank:</span> Sonnfelder Bank<br>
      <span class="label">IBAN:</span> DE139817325500XXXXXXXX<br>
      <span class="label">BIC:</span> GENODES1QTR
    </p>
  </footer>
</main>
</body>
</html>
```